Velvet Shakers business card

We would like a business card designed for our business velvet shakers

We need it to have 2 sides.

More information about the business can be found at www.velvetshakers-example.net

Industry/Entity Type

Business

```html
<!DOCTYPE html>
<html lang="en">
<head>
<meta charset="utf-8">
<title>Velvet Shakers business card</title>
<link href="https://fonts.googleapis.com/css2?family=Lora:ital,wght@0,400;0,700;1,400;1,700&display=swap" rel="stylesheet">
<style>
  :root {
    --page: #e9e7e3;
    --ink: #101010;
    --charcoal: #2b2b2b;
    --charcoal-deep: #141414;
    --gold: #c9a227;
    --white: #ffffff;
    --soft-white: #f1f1f1;
    --drink-warm: #b5541c;
    --drink-dark: #1c1410;
  }
  * { box-sizing: border-box; margin: 0; padding: 0; }
  html, body { width: 1200px; height: 871px; overflow: hidden; }
  body {
    background: var(--page);
    font-family: "Lora", Georgia, serif;
    position: relative;
  }
  .card {
    position: absolute;
    width: 540px;
    height: 309px;
    border-radius: 26px;
    overflow: hidden;
    box-shadow: 0 10px 30px rgba(0,0,0,0.18);
    top: 281px;
  }

  /* Back side */
  .card--back {
    left: 40px;
    background: linear-gradient(160deg, var(--charcoal) 0%, var(--charcoal-deep) 100%);
  }
  .card--back .brand-name {
    position: absolute;
    left: 34px;
    top: 84px;
    font-size: 30px;
    font-weight: 700;
    color: var(--gold);
    white-space: nowrap;
  }
  .card--back .website {
    position: absolute;
    left: 34px;
    bottom: 30px;
    font-style: italic;
    font-size: 14px;
    color: var(--soft-white);
    letter-spacing: 0.3px;
    white-space: nowrap;
  }
  .drink-photo {
    position: absolute;
    right: 0;
    top: 0;
    width: 236px;
    height: 100%;
    background:
      radial-gradient(circle at 35% 40%, var(--drink-warm) 0%, rgba(181,84,28,0.5) 22%, transparent 45%),
      radial-gradient(circle at 75% 75%, #7a2a1e 0%, transparent 35%),
      linear-gradient(90deg, rgba(20,20,20,1) 0%, var(--drink-dark) 35%, #2a1d14 100%);
  }

  /* Front side */
  .card--front {
    right: 40px;
    background: var(--ink);
  }
  .front-top {
    position: absolute;
    inset: 0 0 auto 0;
    height: 136px;
    background: linear-gradient(180deg, var(--white) 0%, #f4f4f4 100%);
    display: flex;
    align-items: center;
    justify-content: center;
  }
  .front-top .brand-name {
    font-size: 34px;
    font-weight: 700;
    color: var(--gold);
    margin-top: 22px;
    white-space: nowrap;
  }
  .holder {
    position: absolute;
    left: 44px;
    top: 158px;
  }
  .holder-name {
    font-size: 25px;
    font-weight: 700;
    font-style: italic;
    color: var(--gold);
    line-height: 1.1;
  }
  .holder-role {
    font-size: 15px;
    color: var(--white);
    margin-top: 2px;
  }
  .contacts {
    position: absolute;
    right: 56px;
    top: 212px;
    list-style: none;
  }
  .contacts li {
    display: flex;
    align-items: center;
    gap: 14px;
    font-size: 14px;
    font-style: italic;
    color: var(--soft-white);
    height: 24px;
    white-space: nowrap;
  }
  .contacts svg { width: 13px; height: 13px; flex: none; }
</style>
</head>
<body>
  <section class="card card--back" aria-label="Card back">
    <div class="brand-name">Velvet Shakers</div>
    <div class="website">www.velvetshakers-example.net</div>
    <div class="drink-photo" role="img" aria-label="Photo of an orange cocktail in a tall glass with fruit garnish, pomegranate and pineapple on a dark table"></div>
  </section>

  <section class="card card--front" aria-label="Card front">
    <div class="front-top">
      <div class="brand-name">Velvet Shakers</div>
    </div>
    <div class="holder">
      <div class="holder-name">Marco Delane</div>
      <div class="holder-role">Founder</div>
    </div>
    <ul class="contacts">
      <li>
        <svg viewBox="0 0 13 13" aria-hidden="true"><rect width="13" height="13" rx="2" fill="var(--gold)"/><path d="M4 3.2c.5-.3.9 0 1.1.5l.4 1c.1.3 0 .6-.3.8l-.4.3c.4.9 1.1 1.6 2 2l.3-.4c.2-.3.5-.4.8-.3l1 .4c.5.2.8.6.5 1.1-.4.7-1 1-1.8.8C5.6 8.8 4.2 7.4 3.6 5.4c-.2-.8.1-1.4.4-2.2z" fill="var(--ink)"/></svg>
        <span>0418275390</span>
      </li>
      <li>
        <svg viewBox="0 0 13 13" aria-hidden="true"><rect width="13" height="13" rx="2" fill="var(--gold)"/><path d="M4 3.2c.5-.3.9 0 1.1.5l.4 1c.1.3 0 .6-.3.8l-.4.3c.4.9 1.1 1.6 2 2l.3-.4c.2-.3.5-.4.8-.3l1 .4c.5.2.8.6.5 1.1-.4.7-1 1-1.8.8C5.6 8.8 4.2 7.4 3.6 5.4c-.2-.8.1-1.4.4-2.2z" fill="var(--ink)"/></svg>
        <span>0461730284</span>
      </li>
      <li>
        <svg viewBox="0 0 13 13" aria-hidden="true"><rect width="13" height="13" rx="2" fill="var(--gold)"/><rect x="2.5" y="4" width="8" height="5.5" fill="none" stroke="var(--ink)" stroke-width="1"/><path d="M2.5 4l4 3 4-3" fill="none" stroke="var(--ink)" stroke-width="1"/></svg>
        <span>info@velvetshakers-example.net</span>
      </li>
    </ul>
  </section>
</body>
</html>
```